I need a camera ready ad
The specs MUST BE as follows
4.875" wide X 8" TALL 300 DPI

WOULD LIKE TO SEE A VERSION WITH ALL in BLACK AND WHITE AND A VERSION IN COLOR
This ad will be going in a playbill for a play

I would like to see if we can get the logo below included in black and white on the downtown skyline followed by the text included.

Independent Film Production company located in the heart of Ferndale, available for all your video production needs. ​We work with our clientele from pre-production including conception, script writing, storyboarding, casting and talent selection through post production to ensure our client’s goals are brought to life​ with engaging visual content that connects with your audiences​. ​ We pride ourselves on helping artists bring their inspiration to life​. We deliver the highest quality productions while keeping costs low for clients. Contact us for ​narrative ​film, ​documentaries and ​commercial ​production ​services.

Gerald Toskin - Executive Producer/President of Brass Meadow Productions is an ​Independent film producer who is passionate about making a difference through the art of motion picture and helping other artists reach their dreams.

Location
Brass Meadow Productions
47 Marlow street
New York NY 10027
Email: BrassMeadowProductions@quillpost.net
Website: www.BrassMeadowProductions.net

Industry/Entity Type

Artists

Colors
171717
ffffff

```html
<!DOCTYPE html>
<html lang="en">
<head>
<meta charset="utf-8">
<title>Brass Meadow Productions – Playbill Ad</title>
<link rel="stylesheet" href="https://fonts.googleapis.com/css2?family=Questrial&display=swap">
<style>
  :root {
    --ink: #171717;
    --paper: #ffffff;
    --band: #4f4f4f;
    --sky-light: #e4e4e4;
    --sky-mid: #9a9a9a;
    --sky-dark: #2e2e2e;
  }
  * { margin: 0; padding: 0; box-sizing: border-box; }
  html, body {
    width: 732px;
    height: 1200px;
    overflow: hidden;
    background: var(--paper);
  }
  .ad {
    position: relative;
    width: 732px;
    height: 1200px;
    background: var(--paper);
    color: var(--ink);
    font-family: "Questrial", "Century Gothic", sans-serif;
  }
  .brand {
    position: absolute;
    top: 34px;
    left: 0;
    width: 100%;
    text-align: center;
  }
  .brand-mark {
    display: block;
    margin: 0 auto 14px;
  }
  .brand-name {
    font-size: 40px;
    line-height: 1;
    color: var(--ink);
    letter-spacing: 0.5px;
  }
  .brand-sub {
    margin-top: 10px;
    font-size: 17px;
    letter-spacing: 5px;
    color: var(--ink);
  }
  .skyline {
    position: absolute;
    top: 270px;
    left: 0;
    width: 732px;
    height: 262px;
    background: linear-gradient(180deg,
      var(--sky-light) 0%,
      var(--sky-mid) 35%,
      var(--sky-dark) 65%,
      var(--sky-mid) 82%,
      var(--sky-light) 100%);
  }
  .copy {
    position: absolute;
    top: 553px;
    left: 46px;
    width: 645px;
    font-size: 19.5px;
    line-height: 33.6px;
  }
  .copy p + p { margin-top: 33.6px; }
  .footer {
    position: absolute;
    left: 0;
    bottom: 0;
    width: 732px;
    height: 98px;
    background: var(--band);
    color: var(--paper);
    text-align: center;
  }
  .footer-address {
    padding-top: 18px;
    font-size: 20px;
    line-height: 28px;
  }
  .footer-contact {
    margin-top: 8px;
    font-size: 15.5px;
    line-height: 22px;
  }
  .sep { padding: 0 6px; }
</style>
</head>
<body>
  <div class="ad">
    <header class="brand">
      <svg class="brand-mark" width="90" height="90" viewBox="0 0 90 90" aria-hidden="true">
        <circle cx="45" cy="45" r="40" fill="none" stroke="var(--ink)" stroke-width="4"/>
      </svg>
      <div class="brand-name">Brass Meadow</div>
      <div class="brand-sub">PRODUCTIONS</div>
    </header>

    <div class="skyline" role="img" aria-label="Black and white photograph of the downtown city skyline across the river"></div>

    <section class="copy">
      <p>Independent Film Production company located in the heart of Ferndale, available for all your video production needs. We work with our clientele from pre-production including conception, script writing, storyboarding, casting and talent selection through post production to ensure our client’s goals are brought to life with engaging visual content that connects with your audiences. We pride ourselves on helping artists bring their inspiration to life. We deliver the highest quality productions while keeping costs low for clients. Contact us for narrative film, documentaries and commercial production services.</p>
      <p>Gerald Toskin - Executive Producer/President of Brass Meadow Productions is an Independent film producer who is passionate about making a difference through the art of motion picture and helping other artists reach their dreams.</p>
    </section>

    <footer class="footer">
      <div class="footer-address">Brass Meadow Productions<span class="sep">|</span>47 Marlow Street<span class="sep">|</span>New York, NY 10027</div>
      <div class="footer-contact">BrassMeadowProductions@quillpost.net<span class="sep">|</span>www.BrassMeadowProductions.net</div>
    </footer>
  </div>
</body>
</html>
```